CD Zipper Mailer Design

I need a zipper mailing envelope designed to hold a cd. I've attached a copy of the actual cd design that is going into the envelope so you can understand the style.

The text for the inside cover should read: "Seven Sales Blunders Every Roofing Contractor Keeps Repeating"
Listen to this interview in full to discover:
- The two types of advertising and why 98% of HVAC business are doing it wrong. Are you one of them?
- The price war that is occuring in the market at present and how you can stand out from the crowd.
- How to get a fast injection of cash if you are currently struggling to make ends meet.

The outside of cover of the design should incorporate my logo and aspects of the style of the cd design itself.

Templates, logos and examples are attached.

So there is 2 template designs that need completing. Sorry is this wasn't clear earlier.

Target Market(s)

HVAC (heating and cooling) business owners

Industry/Entity Type

Advertising

Requirements
Must have
• The text on the inside cover
My logo and business name

```html
<!DOCTYPE html>
<html lang="en">
<head>
<meta charset="utf-8">
<title>Envelope Reverse – Seven Sales Blunders</title>
<link href="https://fonts.googleapis.com/css2?family=Encode+Sans+Condensed:wght@300;400&family=PT+Sans:wght@700&family=Roboto+Condensed:ital,wght@1,700&family=Signika:wght@300&display=swap" rel="stylesheet">
<style>
  :root {
    --page: #ffffff;
    --frame: #8a8a8a;
    --brand-blue: #1f5f9e;
    --body-grey: #8c8c8c;
    --heading-blue: #2a6db3;
    --headline-yellow: #f6c500;
    --title-red: #e8101e;
    --ink: #111111;
    --white: #ffffff;
    --brick: #b8543e;
    --brick-dark: #8f4232;
    --mortar: #9a9388;
    --scale-white: #f1f3f6;
  }
  html, body {
    margin: 0;
    padding: 0;
    width: 1200px;
    height: 1000px;
    overflow: hidden;
    background: var(--page);
  }
  .canvas {
    position: relative;
    width: 1200px;
    height: 1000px;
  }
  .envelope {
    position: absolute;
    left: 125px;
    top: 252px;
    width: 950px;
    height: 511px;
    border: 1px solid var(--frame);
    background: var(--page);
    overflow: hidden;
  }
  .envelope__photo {
    position: absolute;
    left: 210px;
    top: 0;
    width: 740px;
    height: 511px;
  }
  .brand {
    position: absolute;
    left: 30px;
    top: 58px;
    display: flex;
    align-items: center;
    gap: 10px;
    font-family: "PT Sans", sans-serif;
    font-weight: 700;
    font-size: 25px;
    color: var(--brand-blue);
    line-height: 1.1;
  }
  .brand__mark {
    width: 22px;
    height: 22px;
    background: var(--brand-blue);
  }
  .discover {
    position: absolute;
    left: 20px;
    top: 218px;
    width: 240px;
    text-align: center;
    font-family: "Encode Sans Condensed", sans-serif;
  }
  .discover__heading {
    margin: 0 0 4px;
    font-weight: 400;
    font-size: 18px;
    line-height: 21px;
    color: var(--heading-blue);
  }
  .discover__list {
    list-style: none;
    margin: 0;
    padding: 0;
  }
  .discover__item {
    font-weight: 300;
    font-size: 13.5px;
    line-height: 21px;
    color: var(--body-grey);
    margin-bottom: 21px;
  }
  .headline {
    position: absolute;
    right: 28px;
    top: 28px;
    margin: 0;
    text-align: right;
    font-family: "PT Sans", sans-serif;
    font-weight: 700;
    font-size: 27px;
    line-height: 26.5px;
    color: var(--headline-yellow);
    text-shadow: 2px 2px 2px rgba(0,0,0,0.75);
  }
  .title {
    position: absolute;
    left: 372px;
    top: 398px;
    margin: 0;
    white-space: nowrap;
    font-family: "Roboto Condensed", sans-serif;
    font-style: italic;
    font-weight: 700;
    font-size: 18.5px;
    letter-spacing: -0.3px;
    transform: rotate(4deg);
    transform-origin: left center;
  }
  .title__lead {
    font-size: 44px;
    color: var(--title-red);
    text-shadow: 1px 1px 3px rgba(255,255,255,0.9);
    margin-right: 4px;
  }
  .title__dark {
    color: var(--ink);
    text-shadow: 0 0 4px rgba(255,255,255,0.95);
  }
  .title__light {
    color: var(--white);
    text-shadow: 2px 2px 2px rgba(0,0,0,0.9);
  }
  .caption {
    position: absolute;
    left: 0;
    width: 1160px;
    top: 808px;
    text-align: center;
    font-family: "Signika", sans-serif;
    font-weight: 300;
    font-size: 25px;
    color: var(--ink);
  }
</style>
</head>
<body>
<div class="canvas">
  <section class="envelope">
    <svg class="envelope__photo" viewBox="0 0 740 511" role="img" aria-label="Close-up photograph of a thermometer scale against a red brick wall">
      <defs>
        <linearGradient id="photoTone" x1="0" y1="0" x2="1" y2="0">
          <stop offset="0" stop-color="#ffffff" stop-opacity="0"/>
          <stop offset="0.12" stop-color="#eef1f6"/>
          <stop offset="0.36" stop-color="#f1f3f6"/>
          <stop offset="0.40" stop-color="#c0624a"/>
          <stop offset="0.7" stop-color="#b8543e"/>
          <stop offset="1" stop-color="#a44a37"/>
        </linearGradient>
      </defs>
      <rect width="740" height="511" fill="url(#photoTone)"/>
    </svg>

    <div class="brand"><span class="brand__mark"></span>ComfortCrest Growth</div>

    <div class="discover">
      <h2 class="discover__heading">Listen to this interview in full to discover:</h2>
      <ul class="discover__list">
        <li class="discover__item">- The two types of advertising and why 98% of HVAC business are doing it wrong. Are you one of them?</li>
        <li class="discover__item">- The price war that is occuring in the market at present and how you can stand out from the crowd.</li>
        <li class="discover__item">- How to get a fast injection of cash if you are currently struggling to make ends meet.</li>
      </ul>
    </div>

    <h1 class="headline">It’s time<br>to take the temperature<br>of your business<br>performance</h1>

    <p class="title"><span class="title__lead">Seven</span><span class="title__dark">Sales Blunders Every </span><span class="title__light">Roofing Contractor Keeps Repeating</span></p>
  </section>

  <div class="caption">Envelope -Reverse-</div>
</div>
</body>
</html>
```